Poster design for - Rising Maple Gathering

To design a dynamic illustrated Rising Maple Gathering poster.
The dates are: 3-5 July 2020
Location: Tarn Campsite, Henlow, Bedfordshire
www.risingmaple.co.uk

Here is some text about the event to give you an idea. You can take elements from it if you like:

A Gathering of Female Energy to Ignite and Embrace the Power of Woman with Mother Earth.

Target Market(s)

Women festival goers.

Industry/Entity Type

Festival

Colors

Designer to choose colors to be used in the design.

Requirements
Must have
• Rising Maple Logo - but this can be altered to look washed out.
• Date, location, website url.
Nice to have
• Earthy, hippy, festival look.

```html
<!DOCTYPE html>
<html lang="en">
<head>
<meta charset="utf-8">
<title>Rising Maple Gathering</title>
<link rel="stylesheet" href="https://fonts.googleapis.com/css2?family=Didact+Gothic&family=Questrial&display=swap">
<style>
  :root {
    --sky-top: #2c5f9c;
    --sky-mid: #2f72b8;
    --sky-low: #8fa9cf;
    --blush: #efc4bb;
    --title-white: #f4f6f8;
    --ink: #1c1c22;
    --core-red: #e0381c;
    --core-magenta: #c0157a;
    --ring-blue: #3f4fd0;
    --ring-cyan: #6fd0e6;
    --ring-yellow: #e9c92e;
    --ring-orange: #e08a2a;
    --ring-green: #86e07a;
  }
  * { margin: 0; padding: 0; box-sizing: border-box; }
  html, body { width: 800px; height: 1200px; overflow: hidden; }
  .poster {
    position: relative;
    width: 800px;
    height: 1200px;
    overflow: hidden;
    font-family: "Didact Gothic", sans-serif;
    color: var(--ink);
  }
  .backdrop {
    position: absolute;
    inset: 0;
    background: linear-gradient(180deg, var(--sky-top) 0%, var(--sky-mid) 40%, var(--sky-low) 72%, var(--blush) 100%);
  }
  .title {
    position: absolute;
    top: 38px;
    left: 0;
    width: 800px;
    text-align: center;
    font-family: "Questrial", sans-serif;
    color: var(--title-white);
    font-size: 62px;
    line-height: 74px;
    letter-spacing: 2px;
    text-transform: uppercase;
  }
  .feature-art {
    position: absolute;
    left: 104px;
    top: 226px;
    width: 624px;
    height: 830px;
    border-radius: 46% 40% 44% 50%;
    background: radial-gradient(circle at 48% 49%,
      var(--core-red) 0%, var(--core-magenta) 9%, var(--ring-blue) 20%,
      var(--ring-cyan) 30%, var(--ring-yellow) 42%, var(--ring-orange) 55%,
      var(--ring-green) 72%, var(--ring-yellow) 100%);
  }
  .event-details {
    position: absolute;
    left: 76px;
    top: 906px;
  }
  .event-date {
    font-size: 32px;
    font-weight: 700;
    -webkit-text-stroke: 0.6px var(--ink);
    letter-spacing: 0.5px;
    margin-bottom: 12px;
  }
  .event-venue {
    font-size: 20px;
    line-height: 24px;
    -webkit-text-stroke: 0.3px var(--ink);
  }
  .event-url {
    position: absolute;
    left: 76px;
    top: 1124px;
    font-size: 19px;
    -webkit-text-stroke: 0.3px var(--ink);
    letter-spacing: 0.3px;
  }
  .brand-mark {
    position: absolute;
    left: 560px;
    top: 1074px;
    width: 180px;
    text-align: center;
  }
  .brand-dot {
    display: block;
    width: 34px;
    height: 34px;
    margin: 0 auto 12px;
    border-radius: 50%;
    background: var(--ink);
  }
  .brand-name {
    font-size: 27px;
    letter-spacing: 1.5px;
    text-transform: uppercase;
    color: var(--ink);
  }
</style>
</head>
<body>
  <main class="poster">
    <div class="backdrop" role="img" aria-label="Blue to blush gradient background with flowing wavy stripes"></div>

    <h1 class="title">Rising Maple<br>Gathering</h1>

    <div class="feature-art" role="img" aria-label="Illustrated woman's profile silhouette filled with a radiating rainbow kaleidoscope pattern"></div>

    <section class="event-details">
      <p class="event-date">3-5 July 2020</p>
      <p class="event-venue">Tarn Campsite<br>Henlow, Bedfordshire</p>
    </section>

    <p class="event-url">www.risingmaple.co.uk</p>

    <div class="brand-mark">
      <span class="brand-dot"></span>
      <span class="brand-name">Rising Maple</span>
    </div>
  </main>
</body>
</html>
```